Business Card for Lorena Whitfield

Name: Lorena Whitfield
Title: Realtor
Email: Lorena@LorenaWhitfieldRE.com
Phone: 480-555-0137

On the front of the business card, I would like the photo, the contact information and the Lorena Whitfield Logo. The backside is required to have the Broker logo and the required logos. Please use the colors from the logo design. Our company has a classy, professional look.

```html
<!DOCTYPE html>
<html lang="en">
<head>
<meta charset="utf-8">
<title>Lorena Whitfield – Business Card</title>
<link rel="stylesheet" href="https://fonts.googleapis.com/css2?family=Cinzel:wght@400;500&family=Montserrat:wght@400;500&display=swap">
<style>
  :root {
    --backdrop: #3a3a3b;
    --card: #1b1b1c;
    --card-edge: #c0182e;
    --accent: #c8233a;
    --ink-light: #f2f2f2;
    --ink-muted: #3a3a3c;
    --photo-top: #6e6e6e;
    --photo-bottom: #1f1f1f;
  }
  * { box-sizing: border-box; margin: 0; padding: 0; }
  html, body { width: 1200px; height: 801px; overflow: hidden; }
  body {
    background: var(--backdrop);
    position: relative;
    font-family: "Montserrat", Arial, sans-serif;
  }
  .card {
    position: absolute;
    width: 540px;
    height: 309px;
    background: var(--card);
    border-bottom: 3px solid var(--card-edge);
    overflow: hidden;
  }
  .card--front { left: 40px; top: 246px; }
  .card--back  { left: 620px; top: 246px; }

  /* Front */
  .text-panel {
    position: absolute;
    left: 0; top: 0;
    width: 290px; height: 306px;
  }
  .portrait {
    position: absolute;
    right: 0; top: 0;
    width: 250px; height: 306px;
    background: radial-gradient(ellipse at 45% 30%, var(--photo-top) 0%, #3b3b3b 45%, var(--photo-bottom) 85%);
  }
  .brand {
    position: absolute;
    left: 32px; top: 48px;
    display: flex; align-items: center; gap: 12px;
  }
  .brand__mark {
    width: 34px; height: 34px;
    border: 2px solid var(--accent);
    flex: none;
  }
  .brand__text { display: flex; flex-direction: column; width: 190px; }
  .brand__name {
    font-family: "Cinzel", Georgia, serif;
    font-weight: 400;
    color: var(--accent);
    font-size: 17px;
    letter-spacing: 0.5px;
    line-height: 1.1;
    text-transform: uppercase;
    white-space: nowrap;
  }
  .brand__rule {
    height: 1px;
    background: var(--ink-light);
    margin: 3px 0 2px;
    width: 120px;
  }
  .brand__tagline {
    font-family: "Cinzel", Georgia, serif;
    color: var(--ink-light);
    font-size: 8px;
    letter-spacing: 1px;
    text-transform: uppercase;
    align-self: flex-end;
    margin-top: -9px;
  }
  .agent { position: absolute; left: 32px; top: 132px; }
  .agent__name {
    font-family: "Cinzel", Georgia, serif;
    color: var(--accent);
    font-size: 18px;
    letter-spacing: 1px;
    text-transform: uppercase;
    white-space: nowrap;
  }
  .agent__title { color: var(--ink-light); font-size: 13px; margin-top: 2px; }
  .contact { position: absolute; left: 32px; top: 208px; list-style: none; }
  .contact__item {
    display: flex; align-items: center; gap: 9px;
    color: var(--ink-light); font-size: 13px; line-height: 22px;
    white-space: nowrap;
  }
  .contact__icon { width: 12px; height: 12px; flex: none; }

  /* Back */
  .broker {
    position: absolute;
    left: 0; right: 0; top: 78px;
    display: flex; flex-direction: column; align-items: center; gap: 14px;
  }
  .broker__seal {
    width: 100px; height: 100px;
    border-radius: 50%;
    border: 2px solid var(--ink-muted);
  }
  .broker__name {
    font-family: "Cinzel", Georgia, serif;
    color: var(--ink-muted);
    font-size: 26px;
    letter-spacing: 2px;
    text-transform: uppercase;
    text-align: center;
    line-height: 1.1;
  }
  .broker__tagline {
    font-family: "Cinzel", Georgia, serif;
    color: var(--ink-muted);
    font-size: 14px;
    letter-spacing: 2px;
    text-transform: uppercase;
    margin-top: -10px;
  }
  .badges {
    position: absolute; right: 24px; bottom: 22px;
    display: flex; gap: 6px; align-items: center;
  }
  .badge { background: var(--ink-light); height: 22px; }
  .badge--housing { width: 26px; }
  .badge--realtor { width: 22px; }
  .badge--listing { width: 40px; height: 16px; }
</style>
</head>
<body>
  <section class="card card--front">
    <div class="portrait" role="img" aria-label="Black and white portrait photo of the agent"></div>

    <div class="text-panel">
      <div class="brand">
        <span class="brand__mark"></span>
        <div class="brand__text">
          <span class="brand__name">Lorena Whitfield</span>
          <span class="brand__rule"></span>
          <span class="brand__tagline">Real Estate</span>
        </div>
      </div>

      <div class="agent">
        <p class="agent__name">Lorena Whitfield</p>
        <p class="agent__title">Realtor</p>
      </div>

      <ul class="contact">
        <li class="contact__item">
          <svg class="contact__icon" viewBox="0 0 12 12"><path fill="#c8233a" d="M2.5 1 L4.5 1 L5.2 3.5 L4 4.5 Q5 7 7.5 8 L8.5 6.8 L11 7.5 L11 9.5 Q10.5 11 9 11 Q1 10 1 2.5 Q1 1 2.5 1 Z"/></svg>
          480-555-0137
        </li>
        <li class="contact__item">
          <svg class="contact__icon" viewBox="0 0 12 12"><rect x="0.5" y="2" width="11" height="8" fill="#c8233a"/><path d="M0.5 2 L6 6.5 L11.5 2" fill="none" stroke="#1b1b1c" stroke-width="1"/></svg>
          Lorena@LorenaWhitfieldRE.com
        </li>
        <li class="contact__item">
          <svg class="contact__icon" viewBox="0 0 12 12"><circle cx="6" cy="6" r="5.5" fill="#c8233a"/><path d="M0.5 6 H11.5 M6 0.5 Q2.5 6 6 11.5 M6 0.5 Q9.5 6 6 11.5" fill="none" stroke="#1b1b1c" stroke-width="0.8"/></svg>
          www.LorenaWhitfieldRE.com
        </li>
      </ul>
    </div>
  </section>

  <section class="card card--back">
    <div class="broker">
      <span class="broker__seal"></span>
      <p class="broker__name">Harlan Reeves</p>
      <p class="broker__tagline">Real Estate</p>
    </div>
    <div class="badges">
      <span class="badge badge--housing"></span>
      <span class="badge badge--realtor"></span>
      <span class="badge badge--listing"></span>
    </div>
  </section>
</body>
</html>
```